Postcard Design

Pelumint Frozen Yogurt -- small frozen yogurt/soft serve shop inside Larkwood Plaza. We also have cookies, smoothies and coffee. Frozen Yogurt is self-serve with topping bar and priced by weight. We're locally owned and our cookies and yogurt are all hand made at the store.

We'd like to create a postcard containing 3 or 4 coupons for distribution via direct mail, inclusion in event participant gift bags, etc.

Design-wise, our logo and store feature bright colors (lime green, fuscia, dark purple, orange...) but I'd like to quiet down the overall look of the piece with possibly a brown paper bag and bright accents feel. I'd like the look of the piece to suggest a healthy, quality product.

coupon options: Buy one get one free (equal or lesser value) // save $1 // free waffle cone with froyo purchase // 50% off smoothie

```html
<!DOCTYPE html>
<html lang="en">
<head>
<meta charset="utf-8">
<title>Pelumint Frozen Yogurt – Postcard</title>
<link href="https://fonts.googleapis.com/css2?family=Lato:ital,wght@0,400;0,700;0,900;1,400;1,700;1,900&display=swap" rel="stylesheet">
<style>
  :root {
    --lime: #7cbc3c;
    --purple: #9b59ad;
    --purple-dark: #7e3f93;
    --ink: #333333;
    --body-text: #4a4a4a;
    --white: #ffffff;
    --paper: #f1f1f1;
    --stamp: #d2d2d2;
    --backdrop: #e9e6e1;
  }
  * { margin: 0; padding: 0; box-sizing: border-box; }
  html, body { width: 900px; height: 1200px; overflow: hidden; }
  body { background: var(--backdrop); font-family: "Lato", sans-serif; position: relative; }

  .postcard {
    position: absolute; left: 138px; width: 625px; height: 482px;
    background: var(--white); overflow: hidden;
    box-shadow: 0 4px 10px rgba(0,0,0,.18);
  }
  .postcard--front { top: 80px; }
  .postcard--back { top: 625px; }
  .postcard__shapes { position: absolute; inset: 0; }

  .brand { position: absolute; display: flex; align-items: center; gap: 12px; }
  .brand__dot { width: 44px; height: 44px; border-radius: 50%; background: var(--lime); }
  .brand__name { font-weight: 700; font-size: 38px; color: var(--purple-dark); letter-spacing: .5px; }
  .postcard--front .brand { left: 24px; top: 24px; }
  .postcard--back .brand { left: 32px; top: 45px; }

  .headline { position: absolute; color: var(--white); font-style: italic; }
  .headline__lead { display: block; font-weight: 400; }
  .headline__place { display: block; font-weight: 700; }
  .postcard--front .headline { left: 24px; top: 118px; }
  .postcard--front .headline__lead { font-size: 17px; }
  .postcard--front .headline__place { font-size: 25px; margin-top: 2px; }
  .postcard--back .headline { left: 28px; top: 192px; }
  .postcard--back .headline__lead { font-size: 21px; }
  .postcard--back .headline__place { font-size: 34px; margin-top: 4px; }

  .coupon {
    position: absolute; top: 183px; width: 110px; height: 110px; border-radius: 50%;
    background: var(--white); border: 5px solid var(--lime);
    box-shadow: 0 2px 5px rgba(0,0,0,.2);
    display: flex; flex-direction: column; align-items: center; justify-content: center;
    text-align: center; font-style: italic; line-height: 1.05;
  }
  .coupon__accent { color: var(--purple); font-weight: 700; }
  .coupon__strong { color: var(--ink); font-weight: 900; }
  .coupon--bogo { left: 40px; }
  .coupon--save { left: 177px; }
  .coupon--cone { left: 321px; }
  .coupon--smoothie { left: 474px; }

  .intro {
    position: absolute; left: 30px; top: 326px; width: 570px;
    font-style: italic; font-size: 14.5px; line-height: 1.45; color: var(--body-text);
  }
  .intro--short {
    left: 27px; top: 320px; width: 180px; font-size: 12.5px; line-height: 1.5; text-align: justify;
  }

  .contact-bar {
    position: absolute; left: 0; bottom: 0; width: 100%; height: 50px;
    display: flex; align-items: center; color: var(--white); font-size: 20px;
  }
  .contact-bar__item { padding: 0 10px; }
  .contact-bar__item:first-child { padding-left: 33px; border-right: 1px solid rgba(255,255,255,.7); }

  .photo-slot { position: absolute; }
</style>
</head>
<body>

<!-- Front of postcard -->
<section class="postcard postcard--front">
  <svg class="postcard__shapes" width="625" height="482" viewBox="0 0 625 482">
    <defs>
      <linearGradient id="frontPaper" x1="0" y1="0" x2="0" y2="1">
        <stop offset="0" stop-color="#e8e8e8"/><stop offset="1" stop-color="#ffffff"/>
      </linearGradient>
      <linearGradient id="dessertTones" x1="0" y1="0" x2="1" y2="1">
        <stop offset="0" stop-color="#f3f1ef"/><stop offset=".6" stop-color="#ead6df"/><stop offset="1" stop-color="#c9c2c6"/>
      </linearGradient>
    </defs>
    <rect y="240" width="625" height="190" fill="url(#frontPaper)"/>
    <rect y="233" width="625" height="12" fill="var(--purple)"/>
    <path d="M328 0 H625 V240 H372 Q342 130 328 0 Z" fill="url(#dessertTones)" role="img" aria-label="Photo of a bowl of berry frozen yogurt with blueberries and a wooden spoon"/>
    <path d="M318 0 Q332 140 364 245 L372 245 Q342 130 328 0 Z" fill="var(--purple)"/>
    <path d="M0 100 H330 Q346 140 356 186 H0 Z" fill="var(--lime)"/>
    <rect y="426" width="625" height="4" fill="var(--lime)"/>
    <rect y="432" width="625" height="50" fill="var(--purple)"/>
  </svg>

  <div class="brand"><span class="brand__dot"></span><span class="brand__name">pelumint</span></div>

  <h1 class="headline">
    <span class="headline__lead">Small frozen yogurt/soft serve shop</span>
    <span class="headline__place">inside Larkwood Plaza</span>
  </h1>

  <div class="coupon coupon--bogo">
    <span class="coupon__accent" style="font-size:13px">Buy one</span>
    <span class="coupon__strong" style="font-size:14px;font-style:normal;font-weight:700">Get one</span>
    <span class="coupon__accent" style="font-size:26px">free</span>
  </div>
  <div class="coupon coupon--save">
    <span class="coupon__accent" style="font-size:16px">Save</span>
    <span class="coupon__strong" style="font-size:34px">$1</span>
  </div>
  <div class="coupon coupon--cone">
    <span class="coupon__accent" style="font-size:23px">Free</span>
    <span class="coupon__strong" style="font-size:11px;font-style:normal;font-weight:700">waffle cone</span>
    <span class="coupon__accent" style="font-size:12px">with froyo</span>
    <span class="coupon__strong" style="font-size:11px;font-style:normal;font-weight:700">purchase</span>
  </div>
  <div class="coupon coupon--smoothie">
    <span class="coupon__accent" style="font-size:15px">50% off</span>
    <span class="coupon__strong" style="font-size:17px;font-weight:700">Smoothie</span>
  </div>

  <p class="intro">We also have cookies, smoothies and coffee. Frozen Yogurt is self-serve with topping bar &amp; priced by weight. We're locally owned &amp; our cookies &amp; yogurt are all hand made at the store. Frozen Yogurt is self-serve with topping bar and priced by weight. We're locally owned and our cookies and yogurt are all hand made at the store.</p>

  <div class="contact-bar">
    <span class="contact-bar__item">Visit us at - www.pelumint.com</span>
    <span class="contact-bar__item">Call us at - 123.456.789</span>
  </div>
</section>

<!-- Back of postcard -->
<section class="postcard postcard--back">
  <svg class="postcard__shapes" width="625" height="482" viewBox="0 0 625 482">
    <defs>
      <linearGradient id="backPaper" x1="0" y1="0" x2="1" y2="1">
        <stop offset="0" stop-color="#ffffff"/><stop offset="1" stop-color="#e6e6e6"/>
      </linearGradient>
      <linearGradient id="customerTones" x1="0" y1="0" x2="1" y2="0">
        <stop offset="0" stop-color="#ffffff"/><stop offset=".35" stop-color="#e7ddd6"/><stop offset=".7" stop-color="#d98a84"/><stop offset="1" stop-color="#cfe4e6"/>
      </linearGradient>
    </defs>
    <rect width="625" height="482" fill="url(#backPaper)"/>
    <rect x="540" y="22" width="60" height="60" fill="var(--stamp)"/>
    <path d="M342 0 Q372 80 388 160 L396 160 Q380 80 352 0 Z" fill="var(--purple)"/>
    <path d="M352 0 Q380 80 396 160 L406 160 Q392 80 364 0 Z" fill="var(--lime)"/>
    <path d="M0 160 H392 L406 172 V293 H0 Z" fill="var(--lime)"/>
    <path d="M392 160 L406 172 L392 172 Z" fill="#5e9a2a"/>
    <path d="M207 296 H382 Q374 370 340 428 H207 Z" fill="url(#customerTones)" role="img" aria-label="Photo of a smiling customer enjoying a cup of frozen yogurt"/>
    <path d="M382 296 H388 Q380 372 346 428 H340 Q374 370 382 296 Z" fill="var(--purple)"/>
    <rect y="426" width="625" height="4" fill="var(--lime)"/>
    <rect y="432" width="625" height="50" fill="var(--purple)"/>
  </svg>

  <div class="brand"><span class="brand__dot"></span><span class="brand__name">pelumint</span></div>

  <h2 class="headline">
    <span class="headline__lead">Small frozen yogurt/soft serve shop</span>
    <span class="headline__place">inside Larkwood Plaza</span>
  </h2>

  <p class="intro intro--short">Frozen Yogurt is self-serve with topping bar &amp; priced by weight. We're locally owned &amp; our cookies &amp; yogurt are all hand made at the store.</p>

  <div class="contact-bar">
    <span class="contact-bar__item">Visit us at - www.pelumint.com</span>
    <span class="contact-bar__item">Call us at - 123.456.789</span>
  </div>
</section>

</body>
</html>
```